Coffee Bag Design

Vale of Lanterns is brand of specialty roasted coffee from Uganda. We need a packaging design for a 1 kg gusseted bag. We need the bag to embrace our passion for farmers and their coffee. The final print can have a metallic gold or any other color as part of the appeal.
Target market is foreign buyers, tourists, hotels, restaurants and cafes
Vale of Lanterns is owned by Pelkin Trading Ltd also based in Uganda

• 3D Mockups really help me appreciate the submissions.

```html
<!DOCTYPE html>
<html lang="en">
<head>
<meta charset="utf-8">
<title>Vale of Lanterns – Coffee Bag</title>
<link rel="stylesheet" href="https://fonts.googleapis.com/css2?family=Amatic+SC:wght@700&family=Oswald:wght@500;600&display=swap">
<style>
  :root {
    --backdrop: #e4e4e4;
    --gold-light: #f2d35a;
    --gold: #dcb83c;
    --gold-deep: #b8952a;
    --ink: #2a2626;
    --label-white: #f3f3f3;
    --label-frame: #3a3636;
    --valve: #ece9e2;
  }
  * { margin: 0; padding: 0; box-sizing: border-box; }
  html, body { width: 1200px; height: 900px; overflow: hidden; background: var(--backdrop); }
  .canvas { position: relative; width: 1200px; height: 900px; }

  .bag { position: absolute; left: 345px; top: 60px; width: 510px; height: 780px; display: flex; }

  .gusset {
    position: relative; width: 130px; height: 100%;
    background: linear-gradient(180deg, var(--gold-deep) 0%, var(--gold) 40%, var(--gold-deep) 66%, var(--ink) 66%, var(--ink) 97%, var(--gold-deep) 97%);
  }
  .front {
    position: relative; width: 380px; height: 100%;
    background: linear-gradient(180deg, var(--gold-light) 0%, var(--gold) 66%, var(--ink) 66%, var(--ink) 97%, var(--gold) 97%);
  }

  .leaf-art { position: absolute; right: 0; top: 0; width: 160px; height: 240px;
    background: linear-gradient(160deg, rgba(140,110,40,.45), rgba(140,110,40,.1)); border-bottom-left-radius: 80px; }
  .bean-art { position: absolute; border-radius: 50%; background: rgba(200,165,60,.45); }
  .cup-art { position: absolute; left: 22px; bottom: 18px; width: 90px; height: 80px; border-radius: 45px 45px 30px 30px; background: rgba(200,165,60,.4); }
  .side-art { position: absolute; left: 0; top: 470px; width: 50px; height: 180px; background: linear-gradient(180deg, rgba(140,110,40,.45), rgba(200,165,60,.3)); border-radius: 0 40px 40px 0; }

  .valve { position: absolute; left: 165px; top: 240px; width: 48px; height: 48px; border-radius: 50%;
    background: radial-gradient(circle, #fff 0 30%, var(--valve) 32% 100%); border: 2px solid #cfc9bb; }

  .brand { position: absolute; left: 0; right: 0; top: 318px; text-align: center;
    font-family: "Amatic SC", cursive; font-weight: 700; font-size: 60px; color: var(--ink); letter-spacing: 1px; line-height: 1; }
  .tagline { position: absolute; left: 0; right: 0; top: 384px; text-align: center;
    font-family: "Oswald", sans-serif; font-weight: 600; font-size: 15px; color: var(--ink); font-variant: small-caps; letter-spacing: .5px; }

  .spec-label { position: absolute; left: 60px; top: 430px; width: 265px; height: 250px;
    background: linear-gradient(135deg, #e6e6e6, var(--label-white) 50%, #dcdcdc); padding: 10px; }
  .spec-frame { width: 100%; height: 100%; border: 1.5px solid var(--label-frame); padding: 18px 20px; font-family: "Oswald", sans-serif; color: var(--ink); }
  .origin-tag { background: var(--ink); color: var(--gold); text-align: center; font-weight: 600; font-size: 17px; padding: 4px 0; }
  .roast { text-align: center; font-weight: 600; font-size: 19px; line-height: 1.3; margin-top: 18px; }
  .divider { height: 2px; background: var(--ink); margin: 18px 0 20px; }
  .formats { list-style: none; font-weight: 600; font-size: 14px; padding-left: 20px; }
  .formats li { display: flex; align-items: center; gap: 10px; margin-bottom: 12px; }
  .formats li::before { content: ""; width: 18px; height: 18px; border-radius: 50%; background: var(--gold); }

  .net-weight { position: absolute; left: 0; right: 0; top: 712px; text-align: center;
    font-family: "Oswald", sans-serif; font-weight: 600; font-size: 16px; color: var(--gold); }

  .origin-badge { position: absolute; left: 20px; top: 320px; width: 90px; text-align: center; }
  .flag { width: 62px; height: 62px; margin: 0 auto; border-radius: 50%; overflow: hidden; border: 2px solid #eee; }
  .badge-text { font-family: "Oswald", sans-serif; font-size: 8px; color: var(--ink); margin-top: 6px; line-height: 1.2; }
</style>
</head>
<body>
<div class="canvas">
  <div class="bag">
    <section class="gusset">
      <div class="bean-art" style="left:70px;top:190px;width:50px;height:32px" role="img" aria-label="Engraved coffee bean illustration"></div>
      <div class="origin-badge">
        <svg class="flag" viewBox="0 0 60 60" role="img" aria-label="Uganda flag emblem">
          <rect width="60" height="10" y="0" fill="#000"/>
          <rect width="60" height="10" y="10" fill="#f5c400"/>
          <rect width="60" height="10" y="20" fill="#d21f26"/>
          <rect width="60" height="10" y="30" fill="#000"/>
          <rect width="60" height="10" y="40" fill="#f5c400"/>
          <rect width="60" height="10" y="50" fill="#d21f26"/>
          <circle cx="30" cy="30" r="11" fill="#fff"/>
        </svg>
        <p class="badge-text">Grown, Roasted &amp; Packed in the Republic of Uganda</p>
      </div>
      <div class="side-art" role="img" aria-label="Engraved coffee branch illustration"></div>
    </section>
    <section class="front">
      <div class="leaf-art" role="img" aria-label="Engraved coffee leaves and cherries illustration"></div>
      <div class="valve"></div>
      <h1 class="brand">Lantern Blend</h1>
      <p class="tagline">Sunrise Harvest Roast</p>
      <div class="bean-art" style="left:8px;top:560px;width:50px;height:34px" role="img" aria-label="Engraved coffee bean illustration"></div>
      <div class="bean-art" style="right:8px;top:590px;width:40px;height:30px" role="img" aria-label="Engraved coffee bean illustration"></div>
      <div class="bean-art" style="right:10px;top:700px;width:60px;height:34px" role="img" aria-label="Engraved coffee beans illustration"></div>
      <div class="spec-label">
        <div class="spec-frame">
          <p class="origin-tag">SINGLE ORIGIN</p>
          <p class="roast">MEDIUM<br>DARK ROAST</p>
          <div class="divider"></div>
          <ul class="formats">
            <li>ESPRESSO BEANS</li>
            <li>GROUND COFFEE</li>
          </ul>
        </div>
      </div>
      <div class="cup-art" role="img" aria-label="Engraved coffee cup illustration"></div>
      <p class="net-weight">NET WEIGHT: 1kg</p>
    </section>
  </div>
</div>
</body>
</html>
```